Frameless shower doors web site

Build a web site for information and display past projects. Contact information, type of work done. Customer Reviews. The design purpose is to generate phone calls and email inquirers. Domain name is Southernshowerdoors.comEmail is Brightvalebaths@mailbox-demo.com Profile We Love What We Do!Brightvale Bath Panels & Glass LLC. is committed to excellence in every aspect of our business. We hold a standard of integrity bound by fairness, honesty, and personal responsibility. Our distinction is the quality of service and attention to detail we bring to each project. Above all, we listen to our clients input to provide several design options available from designer glass to hardware. We also service and repair existing shower and tub enclosure. Installation of customer purchased enclosure are available by appointment. and address any concerns.

Target Market(s)

25 to 55 residential customers

Number of Pages Required

4 page

Font styles to use
Sans Serif

Colors

Designer to choose colors to be used in the design.

Requirements
Nice to have
• Looking to drive phone calls for estimating shower projects
Should not have
• Lot of prescriptive words, Clutter

```html
<!DOCTYPE html>
<html lang="en">
<head>
<meta charset="utf-8">
<title>Brightvale Bath Panels &amp; Glass</title>
<link href="https://fonts.googleapis.com/css2?family=Poppins:wght@400;500;600;700&family=Roboto:wght@400;500;700&display=swap" rel="stylesheet">
<style>
:root{
  --blue:#1d5fb0;
  --blue-dark:#123f7c;
  --blue-light:#2f7bd6;
  --orange:#f26a1b;
  --ink:#222;
  --muted:#666;
  --grey-bg:#ececec;
  --footer:#141414;
  --white:#fff;
}
*{box-sizing:border-box;margin:0;padding:0}
html,body{width:1200px;height:5357px;overflow:hidden}
body{position:relative;font-family:"Roboto",sans-serif;color:var(--ink);background:var(--white)}
.abs{position:absolute}
h1,h2,h3,h4{font-family:"Poppins",sans-serif}
.photo{position:absolute}

/* header */
.site-header{position:absolute;top:0;left:0;width:1200px;height:145px;background:var(--white)}
.brand{position:absolute;left:140px;top:28px;display:flex;align-items:center;gap:12px}
.brand-mark{width:22px;height:22px;background:var(--blue)}
.brand-name{font-family:"Poppins",sans-serif;font-weight:600;font-size:30px;color:var(--blue-dark);letter-spacing:1px}
.header-call{position:absolute;left:655px;top:32px;display:flex;align-items:center;gap:10px}
.header-call .ico{width:36px;height:36px;border-radius:50%;background:var(--blue-dark);display:flex;align-items:center;justify-content:center}
.header-call small{display:block;font-size:15px;color:var(--muted)}
.header-call strong{font-size:22px;color:var(--blue-dark)}
.quote-btn{position:absolute;left:888px;top:28px;width:165px;height:44px;border:2px solid var(--blue-dark);border-radius:22px;font:600 15px "Poppins",sans-serif;color:var(--blue-dark);display:flex;align-items:center;justify-content:center;gap:8px}
.main-nav{position:absolute;left:466px;top:96px;display:flex;gap:28px;font:500 17px "Poppins",sans-serif;color:var(--blue-dark)}
.main-nav .active{border-bottom:3px solid var(--blue)}

/* hero */
.hero-photo{left:0;top:145px;width:1200px;height:720px;
  background:
    linear-gradient(180deg,rgba(15,30,55,.30),rgba(15,30,55,.45)),
    radial-gradient(ellipse 260px 200px at 150px 180px,rgba(210,235,215,.95),rgba(210,235,215,0)),
    radial-gradient(ellipse 380px 260px at 920px 330px,rgba(245,245,245,.9),rgba(245,245,245,0)),
    radial-gradient(ellipse 300px 200px at 560px 80px,rgba(200,225,245,.85),rgba(200,225,245,0)),
    linear-gradient(100deg,#b9c4c9 0%,#8a9aa5 30%,#6d7780 55%,#a9a39a 80%,#7a6d62 100%)}
.hero-title{left:0;top:355px;width:1200px;text-align:center;color:var(--white);font-size:54px;font-weight:700;text-shadow:0 2px 8px rgba(0,0,0,.35)}
.hero-text{left:350px;top:432px;width:500px;text-align:center;color:var(--white);font-size:18px;line-height:1.5;text-shadow:0 1px 4px rgba(0,0,0,.4)}
.hero-btn{left:483px;top:522px;width:234px;height:48px;border-radius:24px;background:var(--blue-light);color:var(--white);font:600 21px "Poppins",sans-serif;display:flex;align-items:center;justify-content:center;gap:10px}
.hero-arrow{top:440px;width:22px;height:30px;color:var(--white);font-size:34px;line-height:30px}

/* services */
.services-bg{left:0;top:700px;width:1200px;height:780px}
.section-title{font-size:38px;font-weight:500;text-align:center;width:1200px;left:0}
.section-title b{font-weight:700}
.service{top:975px;width:300px;text-align:center;color:var(--white)}
.service .circle{width:114px;height:114px;border-radius:50%;border:4px solid var(--white);margin:0 auto;display:flex;align-items:center;justify-content:center;background:rgba(255,255,255,.12)}
.service h3{font-size:18px;font-weight:600;margin-top:18px;line-height:1.3;text-transform:uppercase}
.service p{font-size:14px;line-height:1.55;margin-top:10px;opacity:.9}
.service .chev{margin-top:16px;font-size:20px}

/* welcome */
.welcome-photo{left:0;top:1420px;width:545px;height:690px;
  background:
    radial-gradient(ellipse 200px 300px at 170px 380px,rgba(255,255,255,.85),rgba(255,255,255,0)),
    linear-gradient(90deg,rgba(160,200,200,.25) 0%,rgba(160,200,200,0) 40%,rgba(170,205,210,.35) 60%,rgba(170,205,210,0) 100%),
    linear-gradient(160deg,#eef0f1 0%,#cfd5d8 40%,#9aa6ab 75%,#6f7a80 100%)}
.welcome-title{left:590px;top:1595px;font-size:37px;font-weight:500;line-height:1.3;color:var(--ink)}
.welcome-title b{color:var(--blue);font-weight:700}
.welcome-text{left:590px;top:1720px;width:440px;font-size:15px;line-height:1.75;color:var(--muted)}
.outline-btn{height:42px;border:2px solid var(--blue);border-radius:21px;color:var(--blue);font:500 15px "Poppins",sans-serif;display:flex;align-items:center;justify-content:center}

/* products */
.products-title{left:90px;top:2225px;font-size:38px;line-height:1.2;font-weight:400}
.products-title b{font-weight:700}
.products-text{left:90px;top:2335px;width:360px;font-size:15px;line-height:1.75;color:var(--muted)}
.products-main{left:528px;top:2175px;width:635px;height:398px;
  background:
    radial-gradient(ellipse 160px 120px at 110px 330px,rgba(255,255,255,.95),rgba(255,255,255,0)),
    radial-gradient(ellipse 200px 260px at 330px 180px,rgba(225,232,235,.9),rgba(225,232,235,0)),
    radial-gradient(ellipse 140px 200px at 560px 260px,rgba(120,110,100,.55),rgba(120,110,100,0)),
    linear-gradient(90deg,#c9cdd0 0%,#e4e6e7 35%,#b7bec3 60%,#d8d4cc 80%,#8d8a86 100%)}
.side-bar{background:var(--blue)}
.product-card{top:2580px;width:376px;height:338px;overflow:hidden}
.product-card .label{position:absolute;left:0;bottom:0;width:100%;height:56px;background:rgba(0,0,0,.45);color:var(--white);font-size:19px;display:flex;align-items:center;justify-content:center}

/* testimonials */
.clients-bg{left:36px;top:2928px;width:1128px;height:450px;background:var(--grey-bg)}
.review{top:3100px;width:300px}
.review .quote{position:absolute;left:0;top:-6px;font:700 34px "Poppins",sans-serif;color:#555}
.review p{margin-left:40px;font-size:14px;line-height:1.6;color:var(--muted)}
.review .who{display:flex;align-items:center;gap:14px;margin-top:22px}
.review .avatar{width:66px;height:66px;border-radius:50%;background:radial-gradient(circle at 50% 40%,#d9c2ae,#6d7f96 70%);border:3px solid var(--white)}
.review .who b{display:block;color:var(--blue);font-size:15px;font-weight:500}
.review .who span{font-size:14px;color:var(--muted)}
.review .stars{color:var(--orange);font-size:15px;letter-spacing:2px}

/* email */
.email-bg{left:0;top:3415px;width:1200px;height:695px;
  background:
    radial-gradient(ellipse 300px 200px at 200px 500px,rgba(110,160,220,.45),rgba(110,160,220,0)),
    radial-gradient(ellipse 260px 300px at 1050px 300px,rgba(90,140,210,.4),rgba(90,140,210,0)),
    linear-gradient(180deg,#1b529c 0%,#174886 50%,#1d5ba8 100%)}
.field{left:310px;width:580px;height:42px;border:1px solid rgba(255,255,255,.5);background:rgba(255,255,255,.12);color:var(--white);font-size:13px;padding:0 14px;display:flex;align-items:center}
.submit{left:310px;top:3920px;width:580px;height:54px;background:var(--orange);color:var(--white);font:600 18px "Poppins",sans-serif;display:flex;align-items:center;justify-content:center}

/* blog */
.blog-photo{left:143px;top:4313px;width:400px;height:312px;
  background:
    radial-gradient(ellipse 120px 100px at 80px 70px,rgba(230,245,255,.95),rgba(230,245,255,0)),
    radial-gradient(ellipse 130px 160px at 260px 190px,rgba(70,80,90,.5),rgba(70,80,90,0)),
    linear-gradient(135deg,#e3e8ec 0%,#b9c3ca 45%,#8c97a0 75%,#5e6870 100%);
  box-shadow:0 6px 18px rgba(0,0,0,.2)}
.blog-title{left:610px;top:4315px;width:460px;font-size:29px;font-weight:600;line-height:1.3}
.blog-meta{left:610px;top:4418px;font-size:14px;color:var(--muted);display:flex;gap:30px}
.blog-text{left:610px;top:4460px;width:460px;font-size:14px;line-height:1.7;color:var(--muted)}
.slider-arrow{top:4440px;font-size:46px;color:#bbb}

/* footer */
.footer-bg{left:0;top:4870px;width:1200px;height:487px;background:var(--footer)}
.footer-brand{left:105px;top:4948px;display:flex;align-items:center;gap:10px;color:var(--white);font:600 26px "Poppins",sans-serif}
.social{left:145px;top:5038px;display:flex;gap:8px}
.social span{width:30px;height:30px;border-radius:50%;border:1.5px solid var(--white)}
.f-head{color:var(--white);font:600 18px "Poppins",sans-serif;text-transform:uppercase}
.f-text{color:#cfcfcf;font-size:14px;line-height:1.6}
.f-list{list-style:none;color:#cfcfcf;font-size:14px;line-height:1.95}
.copy{left:0;top:5275px;width:1200px;text-align:center;color:#cfcfcf;font-size:15px}
</style>
</head>
<body>

<header class="site-header">
  <div class="brand"><span class="brand-mark"></span><span class="brand-name">BRIGHTVALE</span></div>
  <div class="header-call">
    <span class="ico"><svg width="18" height="18" viewBox="0 0 24 24"><path fill="#fff" d="M6.6 10.8a15 15 0 0 0 6.6 6.6l2.2-2.2a1 1 0 0 1 1-.25 11.4 11.4 0 0 0 3.6.57 1 1 0 0 1 1 1V20a1 1 0 0 1-1 1A17 17 0 0 1 3 4a1 1 0 0 1 1-1h3.5a1 1 0 0 1 1 1c0 1.25.2 2.45.57 3.57a1 1 0 0 1-.25 1z"/></svg></span>
    <div><small>Call Us</small><strong>(503) 555-0142</strong></div>
  </div>
  <div class="quote-btn">✎ GET A QUOTE</div>
  <nav class="main-nav"><span class="active">HOME</span><span>ABOUT US</span><span>SERVICES</span><span>GALLERY</span><span>BLOG</span><span>CONTACT US</span></nav>
</header>

<div class="photo hero-photo" role="img" aria-label="Bright modern bathroom with frameless glass shower, window and double vanity"></div>
<div class="abs hero-arrow" style="left:92px">‹</div>
<div class="abs hero-arrow" style="left:1090px">›</div>
<h1 class="abs hero-title">WE LOVE WHAT WE DO!</h1>
<p class="abs hero-text">Sed ut perspiciatis unde omnis iste natus voluptatem accusantium doloremque laudantium</p>
<div class="abs hero-btn"><svg width="22" height="22" viewBox="0 0 24 24"><circle cx="12" cy="12" r="12" fill="#fff"/><path fill="#2f7bd6" d="M8.4 11a8 8 0 0 0 4.6 4.6l1.5-1.5a.7.7 0 0 1 .7-.17 7.9 7.9 0 0 0 2.5.4.7.7 0 0 1 .7.7V17a.7.7 0 0 1-.7.7A11.8 11.8 0 0 1 6.3 5.9a.7.7 0 0 1 .7-.7h2.4a.7.7 0 0 1 .7.7c0 .87.14 1.7.4 2.48a.7.7 0 0 1-.17.7z"/></svg>(503) 555-0142</div>

<svg class="abs services-bg" viewBox="0 0 1200 780" preserveAspectRatio="none">
  <defs><linearGradient id="svcGrad" x1="0" y1="0" x2="0" y2="1"><stop offset="0" stop-color="#1d5fb0" stop-opacity=".92"/><stop offset="1" stop-color="#123f7c"/></linearGradient></defs>
  <polygon points="0,150 500,20 1200,60 1200,780 0,780" fill="url(#svcGrad)"/>
</svg>
<h2 class="abs section-title" style="top:850px;color:#fff"><b>OUR</b> SERVICES</h2>

<div class="abs service" style="left:122px">
  <div class="circle"><svg width="56" height="56" viewBox="0 0 56 56" fill="none" stroke="#fff" stroke-width="3"><rect x="10" y="8" width="36" height="42"/><line x1="28" y1="8" x2="28" y2="50"/><circle cx="20" cy="18" r="3"/></svg></div>
  <h3>Repair Existing<br>Shower</h3>
  <p>Sed ut perspiciatis unde omnis iste natus error sit voluptatem accusantium doloremque laudantium, totam rem aperiam, eaque ipsa quae ab illo inventore</p>
  <div class="chev">︾</div>
</div>
<div class="abs service" style="left:450px">
  <div class="circle"><svg width="56" height="56" viewBox="0 0 56 56" fill="none" stroke="#fff" stroke-width="3"><path d="M8 28h40v8a10 10 0 0 1-10 10H18A10 10 0 0 1 8 36z"/><path d="M14 28V12a5 5 0 0 1 10 0"/><line x1="18" y1="46" x2="16" y2="52"/><line x1="38" y1="46" x2="40" y2="52"/></svg></div>
  <h3>Service Tub<br>Enclosure</h3>
  <p>Sed ut perspiciatis unde omnis iste natus error sit voluptatem accusantium doloremque laudantium, totam rem aperiam, eaque ipsa quae ab illo inventore</p>
  <div class="chev">︾</div>
</div>
<div class="abs service" style="left:778px">
  <div class="circle"><svg width="56" height="56" viewBox="0 0 56 56" fill="none" stroke="#fff" stroke-width="3"><line x1="12" y1="12" x2="44" y2="44"/><line x1="44" y1="12" x2="12" y2="44"/><circle cx="12" cy="12" r="5"/><circle cx="44" cy="12" r="5"/></svg></div>
  <h3>Installation of<br>Purchased Enclosure</h3>
  <p>Sed ut perspiciatis unde omnis iste natus error sit voluptatem accusantium doloremque laudantium, totam rem aperiam, eaque ipsa quae ab illo inventore</p>
  <div class="chev">︾</div>
</div>

<svg class="abs" style="left:0;top:1420px" width="1200" height="690" viewBox="0 0 1200 690"><polygon points="0,60 430,0 1200,60 1200,690 0,690" fill="#f6f6f6"/></svg>
<div class="photo welcome-photo" role="img" aria-label="Walk-in frameless glass shower with white marble tile and bench" style="clip-path:polygon(0 12%,80% 0,100% 4%,100% 100%,0 100%)"></div>
<h2 class="abs welcome-title">WELCOME TO <b>BRIGHTVALE<br>BATH PANELS &amp; GLASS</b></h2>
<p class="abs welcome-text">Sed ut perspiciatis unde omnis iste natus error sit voluptatem accusantium doloremque laudantium, totam rem aperiam, eaque ipsa quae ab illo inventore veritatis et quasi architecto beatae vitae dicta sunt explicabo. Nemo enim ipsam voluptatem quia voluptas sit aspernatur aut odit aut fugit, sed quia consequuntur et quasi architecto beatae vitae dicta sunt explicabo</p>
<div class="abs outline-btn" style="left:588px;top:1938px;width:140px">READ MORE</div>

<h2 class="abs products-title"><b>OUR</b><br>PRODUCTS</h2>
<p class="abs products-text">Sed ut perspiciatis unde omnis iste natus error sit voluptatem accusantium doloremque laudantium, totam rem aperiam, eaque ipsa quae ab illo inventore veritatis et quasi architecto beatae vitae dicta</p>
<div class="abs outline-btn" style="left:90px;top:2475px;width:140px">READ MORE</div>
<div class="abs side-bar" style="left:1163px;top:2175px;width:37px;height:740px"></div>
<div class="abs side-bar" style="left:0;top:2580px;width:36px;height:335px"></div>
<div class="photo products-main" role="img" aria-label="Bright bathroom with freestanding tub, frameless glass shower and marble vanity"></div>
<div class="abs product-card" style="left:36px"><div class="photo" style="inset:0;background:radial-gradient(ellipse 110px 150px at 120px 170px,rgba(250,250,250,.95),rgba(250,250,250,0)),radial-gradient(ellipse 160px 120px at 290px 90px,rgba(120,95,80,.55),rgba(120,95,80,0)),linear-gradient(135deg,#d8c8b8 0%,#b59c88 45%,#7e6a5c 100%)" role="img" aria-label="Glass shower panel beside toilet in warm beige tiled bathroom"></div><div class="label">Quis autem vel eum</div></div>
<div class="abs product-card" style="left:412px"><div class="photo" style="inset:0;background:radial-gradient(ellipse 120px 170px at 190px 150px,rgba(235,238,240,.95),rgba(235,238,240,0)),radial-gradient(ellipse 90px 140px at 330px 200px,rgba(60,62,66,.55),rgba(60,62,66,0)),linear-gradient(135deg,#cfd3d6 0%,#a9afb4 50%,#6e747a 100%)" role="img" aria-label="Corner glass shower with grey mosaic tile and wall fixtures"></div><div class="label">Quis autem vel eum</div></div>
<div class="abs product-card" style="left:788px"><div class="photo" style="inset:0;background:radial-gradient(ellipse 130px 140px at 130px 130px,rgba(225,228,230,.95),rgba(225,228,230,0)),radial-gradient(ellipse 160px 100px at 270px 270px,rgba(45,35,30,.7),rgba(45,35,30,0)),linear-gradient(135deg,#d4d2ce 0%,#a8a39c 50%,#5a514b 100%)" role="img" aria-label="Frameless glass shower enclosure beside dark wood vanity"></div><div class="label">Quis autem vel eum</div></div>

<div class="abs clients-bg"></div>
<h2 class="abs section-title" style="top:2990px"><b>OUR CLIENTS</b> SAYS</h2>
<div class="abs review" style="left:145px"><span class="quote">“</span><p>Sed ut perspiciatis unde omnis iste natus error sit voluptatem accusantium doloremque laudantium, totam rem aperiam, eaque ipsa quae ab illo</p><div class="who"><span class="avatar" role="img" aria-label="Client portrait"></span><div><b>Anna L Reed</b><span>Brightvale Bath</span><div class="stars">★★★★★</div></div></div></div>
<div class="abs review" style="left:465px"><span class="quote">“</span><p>Sed ut perspiciatis unde omnis iste natus error sit voluptatem accusantium doloremque laudantium, totam rem aperiam, eaque ipsa quae ab illo</p><div class="who"><span class="avatar" role="img" aria-label="Client portrait"></span><div><b>Anna L Reed</b><span>Brightvale Bath</span><div class="stars">★★★★★</div></div></div></div>
<div class="abs review" style="left:785px"><span class="quote">“</span><p>Sed ut perspiciatis unde omnis iste natus error sit voluptatem accusantium doloremque laudantium, totam rem aperiam, eaque ipsa quae ab illo</p><div class="who"><span class="avatar" role="img" aria-label="Client portrait"></span><div><b>Anna L Reed</b><span>Brightvale Bath</span><div class="stars">★★★★★</div></div></div></div>

<div class="photo email-bg" role="img" aria-label="Blue-toned bathroom interior with vanity and shower glass"></div>
<h2 class="abs section-title" style="top:3515px;color:#fff"><b>EMAIL</b> INQUIRERS</h2>
<p class="abs" style="left:340px;top:3590px;width:520px;text-align:center;color:#fff;font-size:15px;line-height:1.6">Sed ut perspiciatis unde omnis iste natus error sit voluptatem accusantium doloremque laudantium, totam rem aperiam, eaque ipsa quae</p>
<div class="abs field" style="top:3670px">Name</div>
<div class="abs field" style="top:3720px">Email</div>
<div class="abs field" style="top:3770px">Phone</div>
<div class="abs field" style="top:3820px;height:70px;align-items:flex-start;padding-top:10px">Message</div>
<div class="abs submit">SUBMIT</div>

<h2 class="abs section-title" style="top:4200px;font-weight:500"><b>LATEST</b> BLOG</h2>
<div class="abs slider-arrow" style="left:55px">‹</div>
<div class="abs slider-arrow" style="left:1120px">›</div>
<div class="photo blog-photo" role="img" aria-label="Bathroom with frameless glass shower, window and vanity"></div>
<h3 class="abs blog-title">QUIS AUTEM VEL EUM IURE REPREHENDERIT QUI IN</h3>
<div class="abs blog-meta"><span>▦ March 25, 2019</span><span>◌ 2 Comments</span></div>
<p class="abs blog-text">Sed ut perspiciatis unde omnis iste natus error sit voluptatem accusantium doloremque laudantium, totam rem aperiam, eaque ipsa quae ab illo inventore veritatis et quasi architecto beatae vitae dicta sunt explicabo. Nemo enim ipsam voluptatem quia voluptas sit aspernatur</p>
<div class="abs outline-btn" style="left:610px;top:4585px;width:100px;height:30px;font-size:11px;border-color:#333;color:#333">LEARN MORE</div>

<svg class="abs" style="left:0;top:4748px" width="1200" height="130" viewBox="0 0 1200 130"><polygon points="0,130 560,0 1200,130" fill="#1d5fb0"/><polygon points="0,130 560,20 1200,130" fill="#123f7c"/></svg>
<div class="abs footer-bg"></div>
<div class="abs footer-brand"><span style="width:16px;height:16px;background:#fff;display:inline-block"></span>BRIGHTVALE</div>
<div class="abs social"><span></span><span></span><span></span><span></span></div>

<h4 class="abs f-head" style="left:325px;top:4915px">Contact Us</h4>
<div class="abs f-text" style="left:325px;top:4960px;width:250px">
  <p style="padding-left:32px;position:relative"><svg style="position:absolute;left:0;top:3px" width="16" height="20" viewBox="0 0 16 20"><path fill="#fff" d="M8 0a7 7 0 0 0-7 7c0 5 7 13 7 13s7-8 7-13a7 7 0 0 0-7-7zm0 9.5A2.5 2.5 0 1 1 8 4.5a2.5 2.5 0 0 1 0 5z"/></svg>Brightvale Bath Panels &amp; Glass LLC.<br>410 Harbor Lane Ste 12,<br>Brightvale MI, 48100</p>
  <p style="padding-left:32px;position:relative;margin-top:12px"><svg style="position:absolute;left:0;top:3px" width="16" height="16" viewBox="0 0 24 24"><path fill="#fff" d="M6.6 10.8a15 15 0 0 0 6.6 6.6l2.2-2.2a1 1 0 0 1 1-.25 11.4 11.4 0 0 0 3.6.57 1 1 0 0 1 1 1V20a1 1 0 0 1-1 1A17 17 0 0 1 3 4a1 1 0 0 1 1-1h3.5a1 1 0 0 1 1 1c0 1.25.2 2.45.57 3.57a1 1 0 0 1-.25 1z"/></svg>Phone:<br>(506) 555-0187</p>
  <p style="padding-left:32px;position:relative;margin-top:12px"><svg style="position:absolute;left:0;top:4px" width="16" height="12" viewBox="0 0 16 12"><rect x=".75" y=".75" width="14.5" height="10.5" fill="none" stroke="#fff" stroke-width="1.5"/><path d="M1 1l7 6 7-6" fill="none" stroke="#fff" stroke-width="1.5"/></svg>Email:<br>info@brightvalebaths.com</p>
</div>

<h4 class="abs f-head" style="left:660px;top:4915px">Sign up to receive email</h4>
<p class="abs f-text" style="left:660px;top:4960px;width:290px">Excepteur sint occaecat cupidatat non proident, sunt in culpa qui officia</p>
<div class="abs" style="left:660px;top:5028px;width:275px;height:32px;border-radius:16px;background:#fff;color:#999;font-size:12px;padding:9px 16px">Enter Email</div>
<div class="abs" style="left:660px;top:5072px;width:105px;height:30px;border-radius:15px;background:#1d5fb0;color:#fff;font:600 12px 'Poppins',sans-serif;display:flex;align-items:center;justify-content:center">SUBSCRIBE</div>

<h4 class="abs f-head" style="left:995px;top:4915px">Quick Links</h4>
<ul class="abs f-list" style="left:995px;top:4958px"><li>Home</li><li>Company</li><li>Services</li><li>Projects</li><li>Blog</li><li>Contact</li></ul>

<p class="abs copy">Copyright © Brightvale Bath Panels &amp; Glass LLC. 2019. All rights reserved.</p>

</body>
</html>
```